Modern Website Design for an Online Travel Agency.. Design Only!!

Hi there!

We are building an website for our travel agency that caters to tourists traveling to the Cayman Islands. We provide travel information and take bookings for various tours available here.

We need designs for 8 different web page layouts. You can see the layout specifications in two attached documents. We do not have a need for the coding to be done. This will simply act as a blueprint for our developer to build from.

The important pages are the 'Home Page' 'checkout page' and the ‘Checkout Page’ (Page 1 & 10 in the PDF ‘Website Layout’)

The MOST important page is ‘Tour Search Page’ (page 6)

If you intend on only submitting one page design, please submit a design for page 6. Be aware though, the more of these 3 page designs you submit, the more likely we are to move forward with you!

At this stage, we are simply looking to develop the most aesthetic website design layout possible.

- The website should be colour coordinated with the logo. You can most certainly use other colours if you feel they complement the overall design of the website well.

- Everything must be laid out in an EXTREMELY simple & ‘easy to navigate’ way. The key is simplicity & Functionality. There is no need for messy or elaborate graphics.

- The website MUST have a VERY clean and modern appearance.

- We want the main background to be white, but you can use light grey in places to compliment or add dimension if you feel necessary.

- We will appreciate a good use of shadows and especially a good use of icons. (You can see examples of icons we have already designed, we are definitely open to new icon design concepts too)

- We will reward imagination and original thinking! Essentially we want a website with a creative touch and unique design elements, whilst maintaining that clean and simple layout.

- Most importantly!! - Paying attention to the small details will be highly rewarded (A well balanced and seamless use of fonts, colours, dimensions, shadowing, positioning, etc)

If you have any questions, please don’t hesitate to ask.

We’re excited to see your design submissions!

Thank you!!

You can find all the support documents and content at: https://www.filevorra.net/sh/9qm2rtwplexan7c/QQBmTtZnPdLsWEGxvvaJpLmRw?dl=0

Target Market(s)

Tourists

Industry/Entity Type

Travel

Number of Pages Required

5+ page

Font styles to use
Sans Serif

Colors

Designer to choose colors to be used in the design.

Requirements
Must have
• Must be very clean and modern.
• Must be simple and bold
• Must be color coordinated in a way that makes sense
• White background
Nice to have
• Good use of shadows and Icons
Should not have
• Over use of messy graphics
• And design layout which is not right angled (using anything but vertical or horizontal for the edges in the design)

```html
<!DOCTYPE html>
<html lang="en">
<head>
<meta charset="utf-8">
<title>TripIsla — Plan Your Next Adventure</title>
<link rel="stylesheet" href="https://fonts.googleapis.com/css2?family=Poppins:wght@400;500;600;700;800&display=swap">
<style>
:root{
  --blue:#1f5fd6;
  --green:#8cc63f;
  --ink:#2c3136;
  --muted:#7b8188;
  --canvas:#f4f5f7;
  --card:#eaf2fc;
  --band:#eef5fd;
  --white:#ffffff;
}
*{box-sizing:border-box;margin:0;padding:0}
html,body{width:1200px;height:4481px;overflow:hidden}
body{background:var(--canvas);font-family:'Poppins',sans-serif;color:var(--ink);position:relative}
.page{position:absolute;left:48px;top:46px;width:1104px;height:4386px;background:var(--white);border-top:2px solid var(--blue);border-bottom:2px solid var(--blue)}
.abs{position:absolute}
/* header */
.brand{left:55px;top:36px;display:flex;align-items:center;gap:8px;font-weight:600;font-size:16px;color:var(--blue)}
.brand i{display:block;width:16px;height:16px;background:var(--green);border-radius:3px}
.utility{right:50px;top:8px;display:flex;align-items:center;gap:8px;font-size:9px;font-weight:600}
.dot{width:11px;height:11px;border-radius:50%;border:1.5px solid #6c7278}
.utility .cur{margin-left:16px}
.utility .login{color:var(--blue);margin-left:18px}
.nav{left:333px;top:44px;display:flex;gap:31px;font-size:9px;font-weight:600;letter-spacing:.2px}
.dest-btn{left:966px;top:30px;width:138px;height:40px;background:var(--green);color:#fff;font-size:9px;font-weight:600;display:flex;align-items:center;justify-content:center}
/* hero */
.hero{left:0;top:71px;width:1104px;height:492px;background:linear-gradient(180deg,#3d8f9b 0%,#2aa3a8 40%,#2f8b86 70%,#6b7a52 100%)}
.hero h1{position:absolute;left:0;right:0;top:130px;text-align:center;color:#fff;font-weight:800;font-size:70px;line-height:64px;letter-spacing:-1px}
.btn{display:inline-flex;align-items:center;justify-content:center;border-radius:20px;color:#fff;font-weight:600;font-size:8px;letter-spacing:.3px}
.hero .btn{position:absolute;left:482px;top:366px;width:140px;height:36px;background:var(--green)}
.hero .arrows{position:absolute;left:510px;top:428px;display:flex;gap:12px}
.ring{width:32px;height:32px;border-radius:50%;border:1.5px solid rgba(255,255,255,.8);display:flex;align-items:center;justify-content:center;color:#fff;font-size:13px}
/* sections */
.section-title{left:0;width:1104px;text-align:center;font-weight:600;font-size:35px;line-height:49px}
.rule{width:40px;height:3px;background:var(--green);left:532px}
.lead{left:140px;width:824px;text-align:center;font-size:12.5px;line-height:21.5px;color:var(--muted)}
.lead b{color:var(--green);font-weight:600}
.lead a{color:var(--blue);font-weight:600;text-decoration:none}
.see{left:0;width:1104px;text-align:center;font-size:10px;font-weight:600;color:var(--blue)}
.feature{background:var(--card);border-radius:6px}
.feature h3{position:absolute;font-weight:600;font-size:26px;line-height:27px}
.feature p{position:absolute;width:360px;font-size:12px;line-height:21.5px;color:var(--muted)}
.feature .btn{position:absolute;height:34px;background:var(--blue);padding:0 26px}
.art{position:absolute;width:260px;height:260px;border-radius:50%;background:radial-gradient(circle at 50% 55%,#e6f3ea 0%,#ffffff 70%)}
/* destinations */
.place{height:186px;border-radius:3px;color:#fff;text-align:center;display:flex;flex-direction:column;justify-content:center;padding-top:20px}
.place strong{font-size:18px;font-weight:600}
.place span{font-size:11px;opacity:.9}
.p1{background:linear-gradient(135deg,#1e3d63,#3c6a8c 50%,#243e5c)}
.p2{background:linear-gradient(180deg,#5f8cab 0%,#2f6b3e 35%,#3aa8a0 60%,#58c5c0 100%)}
.p3{background:linear-gradient(135deg,#6f8fae,#3f6d94 50%,#7b99b3)}
/* things to do */
.band{left:0;top:3663px;width:1104px;height:477px;background:var(--band)}
.band h2{position:absolute;left:55px;top:56px;font-size:35px;font-weight:600}
.band .rule{left:55px;top:113px}
.band p{position:absolute;left:55px;top:140px;width:250px;font-size:12px;line-height:21.5px;color:var(--muted)}
.band .arrows{position:absolute;left:55px;top:218px;display:flex;gap:12px}
.band .ring{border-color:var(--blue);color:var(--blue)}
.tour{position:absolute;top:45px;width:235px}
.tour .photo{height:268px}
.tour h4{font-size:17px;font-weight:600;margin-top:14px}
.stars{color:var(--green);font-size:12px;letter-spacing:2px;line-height:16px}
.price{font-size:10px;font-weight:500;margin-top:3px}
.tour .btn{margin-top:20px;height:30px;padding:0 20px;background:var(--blue)}
/* footer */
.foot-brand{left:55px;top:4220px}
.socials{left:55px;top:4252px;display:flex;gap:11px}
.socials .dot{width:16px;height:16px;border-color:var(--ink)}
.copy{left:55px;top:4280px;font-size:8px}
.col{top:4208px;font-size:9.5px;line-height:26px;color:var(--muted)}
.col h5{color:var(--green);font-size:9.5px;font-weight:600}
</style>
</head>
<body>
<div class="page">
  <!-- header -->
  <div class="abs utility"><span class="dot"></span><span class="dot"></span><span class="dot"></span><span class="dot"></span><span class="cur">USD ⌄</span><span class="login">LOGIN</span></div>
  <div class="abs brand"><i></i>TripIsla</div>
  <nav class="abs nav"><span>DISCOVER CAYMAN</span><span>THING TO DO</span><span>MY TRIP PLANNER</span><span>MAP</span><span>CONTACT US</span></nav>
  <div class="abs dest-btn">DESTINATIONS ⌄</div>

  <section class="abs hero" role="img" aria-label="Snorkelers swimming above a coral reef in clear turquoise water">
    <h1>PLAN YOUR NEXT<br>ADVENTURE</h1>
    <span class="btn">DISCOVER NOW ›</span>
    <div class="arrows"><span class="ring">‹</span><span class="ring">›</span></div>
  </section>

  <!-- welcome -->
  <h2 class="abs section-title" style="top:622px">Welcome To TripIsla</h2>
  <div class="abs rule" style="top:677px"></div>
  <p class="abs lead" style="top:700px">We are proud travel concierges of the Cayman Islands! We help thousands of tourists visiting Cayman every year arrange vacation getaway catered to their exact needs. With a wealth of local knowledge, we help you avoid unreliable tour operators and find those local hidden gems. Here you can research everything you need to be fully prepared for your travels and also view the complete range of activities available.</p>
  <div class="abs see" style="top:797px">See More ⊕</div>
  <div class="abs feature" style="left:140px;top:839px;width:824px;height:332px">
    <h3 style="left:65px;top:74px">Explore Where You’re<br>Going</h3>
    <p style="left:65px;top:140px">Use our fully comprehensive guide to learn everything you need to know about travel &amp; safety in the country you’re interested in traveling to.</p>
    <span class="btn" style="left:65px;top:224px">DISCOVER NOW ›</span>
    <div class="art" style="left:499px;top:37px" role="img" aria-label="Illustration of a traveler beside a large map board and suitcase"></div>
  </div>

  <!-- why -->
  <h2 class="abs section-title" style="top:1252px;left:200px;width:704px">Why Should Organizing A Vacation Be So Complicated?</h2>
  <div class="abs rule" style="top:1363px"></div>
  <p class="abs lead" style="top:1383px;left:130px;width:844px">We all know it! Dreaming up a vacation can be tremendous fun. What better than exploring the endless possibilities of your next adventure? But then comes the nitty gritty task of actually pulling a vacation together. How do you decide on the most suitable activities to experience and the best tour operators to guide you? Despite your best efforts to avoid booking mix-ups, well hidden costs or dishonest tour operators, mishaps can occur and sometimes can be detrimental to your experience abroad.</p>
  <div class="abs see" style="top:1503px">See More ⊕</div>
  <div class="abs feature" style="left:140px;top:1545px;width:909px;height:332px">
    <div class="art" style="left:65px;top:36px" role="img" aria-label="Illustration of a person at a laptop surrounded by travel icons"></div>
    <h3 style="left:403px;top:72px">Choose Your Favorite<br>Activities</h3>
    <p style="left:403px;top:138px">Keep the fun of planning and easily budget your entire trip. We’ll deal with the hard work and handle all your booking arrangements</p>
    <span class="btn" style="left:403px;top:222px">FIND THE FUN ›</span>
  </div>

  <!-- proud -->
  <h2 class="abs section-title" style="top:1958px">We’re Proud Of What We Do</h2>
  <div class="abs rule" style="top:2020px"></div>
  <p class="abs lead" style="top:2041px;left:130px;width:844px">We all know that you get the best travel advise from locals. So why wouldn’t you use a local travel agent to help arrange your vacation? We take the time to selectively employ the best agents and concierges from each country to join our team. Our Travel Concierges personally experience every single tour first hand, so they can be in a position to give you the best possible advice and service.</p>
  <div class="abs see" style="top:2138px">See More ⊕</div>
  <div class="abs feature" style="left:140px;top:2182px;width:824px;height:332px">
    <h3 style="left:65px;top:72px">We Make All The<br>Arrangements</h3>
    <p style="left:65px;top:138px">Fill out our simple form and we’ll use our local expertise to design your ideal vacation package. Best of all, our services are 100% FREE!</p>
    <span class="btn" style="left:65px;top:222px">GET A CUSTOM VACATION PROPOSAL ›</span>
    <div class="art" style="left:499px;top:36px" role="img" aria-label="Illustration of a guide greeting a traveler with a suitcase under palm trees"></div>
  </div>

  <!-- not average -->
  <h2 class="abs section-title" style="top:2594px">We’re Not Your Average Travel Agency</h2>
  <div class="abs rule" style="top:2656px"></div>
  <p class="abs lead" style="top:2676px;left:140px;width:824px"><b>Travel Agents</b> can be great as they simplify the process of planning a vacation. But unfortunately their abilities are often limited as usually they’ve never even been to the country you’re looking to go. Once you’re out the office and on the plane, there’s little they can do to look after you. For example, what happens if when bad weather forces you to reschedule your tours?</p>
  <div class="abs see" style="top:2774px">See More ⊕</div>
  <div class="abs feature" style="left:140px;top:2816px;width:824px;height:332px">
    <div class="art" style="left:65px;top:36px" role="img" aria-label="Illustration of people relaxing on a beach with a surfboard and palm leaves"></div>
    <h3 style="left:403px;top:72px">Relax And Enjoy<br>Your Vacation</h3>
    <p style="left:403px;top:138px">Consider us your guardian angels during your stay. We continue to offer support throughout your trip, so you can truly enjoy your vacation, stress free!</p>
    <span class="btn" style="left:403px;top:222px">FIND YOUR TRAVEL ANGEL ›</span>
  </div>

  <!-- destinations -->
  <h2 class="abs section-title" style="top:3230px">Destinations</h2>
  <div class="abs rule" style="top:3291px"></div>
  <p class="abs lead" style="top:3312px;left:140px;width:824px">Don’t miss out on the best activities because you waited last minute. <a>Contact Us</a> now to see how we can help you put together your perfect vacation getaway!</p>
  <div class="abs place p1" style="left:55px;top:3385px;width:320px" role="img" aria-label="Aerial view of Grand Cayman coastline"><strong>Grand Cayman</strong><span>83 Activities</span></div>
  <div class="abs place p2" style="left:392px;top:3385px;width:320px" role="img" aria-label="Tropical island shoreline with turquoise water"><strong>Cayman Brac</strong><span>9 Activities</span></div>
  <div class="abs place p3" style="left:729px;top:3385px;width:320px" role="img" aria-label="Aerial view of a narrow island in deep blue sea"><strong>Cayman Brac</strong><span>9 Activities</span></div>

  <!-- things to do -->
  <section class="abs band">
    <h2>Things To Do</h2>
    <div class="abs rule"></div>
    <p>Don’t miss out on the best activities because you waited last minute.</p>
    <div class="arrows"><span class="ring">‹</span><span class="ring">›</span></div>
    <div class="tour" style="left:392px">
      <div class="photo" role="img" aria-label="Group visiting a historic white wooden mission house" style="background:linear-gradient(180deg,#a9b4bd,#6d7a6a 60%,#8a8f86)"></div>
      <h4>Mission House Tour</h4><div class="stars">★★★★</div><div class="price">99.50 KYD</div>
      <span class="btn">SEE DETAILS ›</span>
    </div>
    <div class="tour" style="left:646px">
      <div class="photo" role="img" aria-label="Museum gallery with historic exhibits" style="background:linear-gradient(180deg,#6a6258,#8c8478 50%,#4f4a44)"></div>
      <h4>Our National Museum</h4><div class="stars">★★★★★</div><div class="price">88.05 KYD</div>
      <span class="btn">SEE DETAILS ›</span>
    </div>
    <div class="tour" style="left:898px;width:206px;overflow:hidden">
      <div class="photo" role="img" aria-label="Rider on horseback along the beach" style="background:linear-gradient(180deg,#7fa9c9,#9bb8c9 45%,#7a5a3e 75%,#c9b79a)"></div>
      <h4>Horseback Riding</h4><div class="stars">★★★★</div><div class="price">204.00 KYD</div>
      <span class="btn">SEE DETAILS ›</span>
    </div>
  </section>

  <!-- footer -->
  <div class="abs brand foot-brand" style="font-size:19px"><i style="width:20px;height:20px"></i>TripIsla</div>
  <div class="abs socials"><span class="dot"></span><span class="dot"></span><span class="dot"></span><span class="dot"></span></div>
  <div class="abs copy">© 2019 TripIsla Ltd. All Rights Reserved.</div>
  <div class="abs col" style="left:375px"><h5>Our Company</h5><div>About us</div><div>How it works?</div><div>Our investors</div><div>Contact us</div><div>Work with us</div></div>
  <div class="abs col" style="left:543px"><h5>Support</h5><div>FAQ</div><div>Legal notices</div><div>Cancellation policy</div><div>Terms of use</div><div>Privacy policy</div></div>
  <div class="abs col" style="left:743px"><h5>Planning Trip</h5><div>My Trip Planner</div><div>Things to Do</div><div>Map</div><div>Discover Cayman</div></div>
</div>
</body>
</html>
```